Massage-Creme label for a young pharmacy

We are a young pharmacy which is part of a big union. We developed for a customer a very good massage creme with aloe vera, coconut oil, and many more advantages and as well a massage jelly. All we need is a good and affordable label which is beatiful and helps us to promote our product. As we want to develop further products, it would be very cool to have a corporate label for all upcoming products.

Target Market(s)

professional masseurs and physiotherapists

Industry/Entity Type

Health And Wellness

Font styles to use
Sans Serif
Decorative

Colors

Designer to choose colors to be used in the design.

Requirements
Must have
• Professionally looking design (but I'm sure you are doing so... :-)
Nice to have
• Label can have any shape. What you see is just a bad label with corresponding sizes, so you can imagine how it would look like in the final state.
Should not have
• If possible, the label should not be completely black (although it might look cool) as we are printing it on our own Varnick tq318-dm and black is difficult to print (and very costy).

```html
<!DOCTYPE html>
<html lang="de">
<head>
<meta charset="utf-8">
<title>Massage Creme Label</title>
<link rel="stylesheet" href="https://fonts.googleapis.com/css2?family=Righteous&family=Luckiest+Guy&display=swap">
<style>
  :root {
    --page: #ffffff;
    --label-green: #3bb04a;
    --frame-green: #1d7a35;
    --deep-green: #17602b;
    --cream: #ffffff;
    --brown: #6b2e12;
    --leaf-green: #1f8a3c;
    --coconut-flesh: #dfe6dc;
  }
  html, body {
    margin: 0;
    padding: 0;
    width: 1200px;
    height: 861px;
    overflow: hidden;
    background: var(--page);
  }
  .label {
    position: absolute;
    left: 380px;
    top: 26px;
    width: 440px;
    height: 808px;
    background: var(--label-green);
  }
  .frame {
    position: absolute;
    inset: 0;
  }
  .brand {
    position: absolute;
    top: 40px;
    left: 0;
    width: 100%;
    text-align: center;
    font-family: "Righteous", sans-serif;
    font-size: 36px;
    letter-spacing: 4px;
    color: var(--deep-green);
    line-height: 38px;
  }
  .brand span {
    background: var(--label-green);
    padding: 0 10px;
  }
  .hands-icon {
    position: absolute;
    left: 150px;
    top: 96px;
    width: 140px;
    height: 76px;
    border-radius: 70px 70px 20px 20px;
    background: linear-gradient(180deg, var(--brown) 0%, var(--brown) 70%, var(--deep-green) 100%);
  }
  .subtitle, .headline {
    position: absolute;
    left: 0;
    width: 100%;
    text-align: center;
    font-family: "Righteous", sans-serif;
    color: var(--cream);
    margin: 0;
  }
  .subtitle {
    top: 194px;
    font-size: 30px;
    letter-spacing: 0.5px;
    text-shadow: 2px 2px 0 var(--brown);
  }
  .headline {
    top: 232px;
    font-size: 74px;
    line-height: 72px;
    letter-spacing: -1px;
    text-shadow: 3px 3px 0 var(--brown), 4px 4px 0 var(--brown);
  }
  .badge {
    position: absolute;
    left: 232px;
    top: 394px;
    width: 158px;
    height: 62px;
    background: var(--brown);
    transform: rotate(-14deg) skewX(-4deg);
    transform-origin: center;
    font-family: "Luckiest Guy", sans-serif;
    color: var(--cream);
    font-size: 19px;
    line-height: 21px;
    text-align: right;
    padding: 9px 12px 0 0;
    box-sizing: border-box;
  }
  .ingredients-art {
    position: absolute;
    left: 104px;
    top: 420px;
    width: 240px;
    height: 230px;
    border-radius: 50% 50% 46% 46%;
    background: radial-gradient(circle at 50% 60%, var(--leaf-green) 0%, var(--coconut-flesh) 38%, var(--brown) 72%);
  }
  .ingredients-name {
    position: absolute;
    left: 0;
    top: 560px;
    width: 440px;
    height: 180px;
  }
  .ingredients-name text {
    font-family: "Luckiest Guy", sans-serif;
    font-size: 28px;
    fill: var(--cream);
    letter-spacing: 1px;
  }
</style>
</head>
<body>
  <main class="label">
    <svg class="frame" width="440" height="808" viewBox="0 0 440 808" aria-hidden="true">
      <g fill="none" stroke="var(--frame-green)" stroke-width="3">
        <polyline points="44,60 44,744 396,744 396,60"/>
        <line x1="30" y1="60" x2="110" y2="60"/>
        <line x1="330" y1="60" x2="410" y2="60"/>
        <line x1="30" y1="744" x2="410" y2="744"/>
      </g>
    </svg>

    <div class="brand"><span>Kelvara</span></div>

    <div class="hands-icon" role="img" aria-label="Two cupped brown hands above a green oil drop"></div>

    <p class="subtitle">PROFESSIONELLE</p>
    <h1 class="headline">MASSAGE<br>CREME</h1>

    <div class="ingredients-art" role="img" aria-label="Halved coconuts with aloe vera leaves and green leaves behind"></div>

    <div class="badge">ENERGETISCH<br>LEITEND!</div>

    <svg class="ingredients-name" viewBox="0 0 440 180" aria-label="Coconut &amp; Aloe Vera">
      <path id="ingredient-arc" d="M60,40 Q210,170 380,40" fill="none"/>
      <text text-anchor="middle"><textPath href="#ingredient-arc" startOffset="50%">COCONUT &amp; ALOE VERA</textPath></text>
    </svg>
  </main>
</body>
</html>
```